Swimming Pool Business Billboard

10' x 24' Billboard displaying company name, logo and phone number. Picture of swimming pool activity; kids playing , swimming, etc. Bullet points possibly shown: New Construction, Repairs, Weekly maintenance.

Industry/Entity Type

Swimming pool construction, repairs and maintenance.

Font styles to use
Sans Serif

Colors
0054AA
0677BA
7BADD7
CADEEF
E8F1F8

Requirements
Must have
• Rusty & Calder Pembrook, RUSTY'S POOLS & Service,
Nice to have
• Prefer to have my last name "Pembrook" above the word "POOLS" only in smaller print so that "RUSTYS POOLS" is distinguished.

```html
<!DOCTYPE html>
<html lang="en">
<head>
<meta charset="utf-8">
<title>Rusty's Pools Billboard</title>
<link href="https://fonts.googleapis.com/css2?family=Anton&family=Poppins:wght@400;600;700&display=swap" rel="stylesheet">
<style>
  :root{
    --navy:#0054AA;
    --deep:#0a3f7c;
    --mid:#0677BA;
    --sky:#7BADD7;
    --pale:#CADEEF;
    --mist:#E8F1F8;
    --water-a:#2fc0f0;
    --water-b:#6fd6fb;
    --white:#ffffff;
  }
  *{margin:0;padding:0;box-sizing:border-box}
  html,body{width:982px;height:1200px;overflow:hidden}
  body{background:var(--mist);font-family:"Poppins",sans-serif;position:relative}
  .billboard{
    position:absolute;left:21px;top:383px;width:940px;height:434px;overflow:hidden;
    background:linear-gradient(160deg,var(--water-b) 0%,var(--water-a) 55%,#1fb2ea 100%);
    box-shadow:0 6px 24px rgba(10,63,124,.25);
  }
  .kid-photo{
    position:absolute;left:0;top:58px;width:300px;height:340px;
    background:radial-gradient(ellipse at 55% 45%,#e9b48c 0%,#d9966a 35%,rgba(126,200,240,.6) 70%,rgba(126,200,240,0) 100%);
  }
  .mascot{
    position:absolute;left:300px;top:150px;width:150px;height:200px;
    background:radial-gradient(ellipse at 50% 50%,var(--navy) 0%,var(--mid) 45%,rgba(255,255,255,.7) 70%,rgba(255,255,255,0) 100%);
    border-radius:50%;
  }
  .owner-name{
    position:absolute;right:18px;top:2px;
    font-family:"Anton",sans-serif;font-weight:400;font-size:56px;line-height:1;letter-spacing:1px;
    color:var(--navy);text-shadow:3px 3px 0 var(--white);white-space:nowrap;
    transform:scaleY(1.9);transform-origin:top right;
  }
  .business-name{
    position:absolute;right:20px;top:140px;
    font-family:"Poppins",sans-serif;font-weight:700;font-size:30px;line-height:1;
    color:var(--white);letter-spacing:.5px;white-space:nowrap;
  }
  .services{
    position:absolute;left:484px;top:232px;display:flex;gap:12px;align-items:center;list-style:none;
  }
  .service{display:flex;align-items:center;gap:6px;color:var(--deep);font-weight:600;font-size:17px;line-height:1.08}
  .service-icon{width:32px;height:32px;border-radius:50%;background:var(--white);display:flex;align-items:center;justify-content:center;flex:none}
  .contact-band{position:absolute;left:0;bottom:0;width:940px;height:116px}
  .address{
    position:absolute;right:24px;bottom:80px;color:var(--white);font-size:20px;font-weight:400;white-space:nowrap;line-height:1.2;
  }
  .phone{
    position:absolute;right:24px;bottom:2px;color:var(--white);font-size:62px;font-weight:700;line-height:1.2;letter-spacing:1px;white-space:nowrap;
  }
  .email{
    position:absolute;left:36px;bottom:4px;color:var(--deep);font-size:27px;font-weight:600;line-height:1.2;white-space:nowrap;
  }
</style>
</head>
<body>
  <section class="billboard">
    <div class="kid-photo" role="img" aria-label="Photo of a smiling child in sunglasses resting on a pool float"></div>
    <div class="mascot" role="img" aria-label="Illustrated sea king mascot holding a trident"></div>

    <h1 class="owner-name">RUSTY &amp; CALDER PEMBROOK</h1>
    <p class="business-name">RUSTY'S POOLS &amp; SERVICE</p>

    <ul class="services">
      <li class="service">
        <span class="service-icon">
          <svg width="20" height="20" viewBox="0 0 20 20"><circle cx="10" cy="10" r="6" fill="none" stroke="#0a3f7c" stroke-width="3"/><rect x="8.5" y="8" width="3" height="11" fill="#0a3f7c"/></svg>
        </span>Repairs
      </li>
      <li class="service">
        <span class="service-icon">
          <svg width="20" height="20" viewBox="0 0 20 20"><path d="M3 15 L9 9 L12 12 L17 5" fill="none" stroke="#0a3f7c" stroke-width="3" stroke-linecap="round"/><rect x="2" y="15" width="10" height="3" fill="#0a3f7c"/></svg>
        </span>New<br>Construction
      </li>
      <li class="service">
        <span class="service-icon">
          <svg width="18" height="18" viewBox="0 0 18 18"><rect x="2" y="3" width="14" height="13" rx="2" fill="#0a3f7c"/><rect x="5" y="1" width="2" height="4" fill="#0a3f7c"/><rect x="11" y="1" width="2" height="4" fill="#0a3f7c"/><text x="9" y="14" font-size="8" fill="#fff" text-anchor="middle" font-family="Poppins,sans-serif">7</text></svg>
        </span>Weekly<br>Maintenance
      </li>
    </ul>

    <svg class="contact-band" viewBox="0 0 940 116" preserveAspectRatio="none" aria-hidden="true">
      <polygon points="0,72 440,72 428,116 0,116" fill="#ffffff"/>
      <polygon points="462,0 940,0 940,116 428,116" fill="#0a3f7c"/>
    </svg>
    <p class="address">2750 harlow Rd brierton, Ga 31599</p>
    <p class="phone">555•014•2290</p>
    <p class="email">rusty@rppools.com</p>
  </section>
</body>
</html>
```